Tilda Tinkerwire, An IT Company Has New Logo, Need Fresh Business Cards

IT company is called Tilda Tinkerwire and is displayed nicely with the new logo from here on pitchloft. Would like a fresh business card look that encompasses the idea that we want clients to Cherish Every Gadget. I love the use of circuitry with hearts as endpoints and x's and o's. It needs to have room for my certification logos of which there are 4 and a BRJ Alumni log. I am attaching my current card to illustrate how it has always captured attention, but that was in the early stages of business when I was doing more residential work. I am focused on businesses now, so a level of professionalism is necessary. I would also like the card to lend itself well to additional stationary, email signature, ticketing template for my workboard, etc. For the time being, I need the card for an upcoming conference so that work will come later. Color scheme should be that of the new logo. Thank you and I look forward to the designs.

Target Market(s)

Businesses looking for IT services.

Industry/Entity Type

Information Technology

Contact Information for Business Card

See above

Requirements
Must have
• New logo colors and a warm feel. Possibly a tad feminine as I am female, but appealing to males.
Nice to have
• I would like techy, but no too much so. I like friendly and connecting feels. People LOVED my old card and called me because it gave them a warm feeling.

```html
<!DOCTYPE html>
<html lang="en">
<head>
<meta charset="utf-8">
<title>Tilda Tinkerwire — Business Card</title>
<link rel="stylesheet" href="https://fonts.googleapis.com/css2?family=Montserrat:wght@400;500;600&display=swap">
<style>
  :root {
    --stage: #3a3a3c;
    --pink: #e596c1;
    --pink-deep: #c889ad;
    --pink-text: #d89ac7;
    --white: #ffffff;
    --paper: #f4f4f4;
    --band: #eeeeee;
    --green: #a9c94f;
    --blue: #5fb3d6;
    --purple: #c39ad0;
    --ink: #333333;
  }
  * { box-sizing: border-box; margin: 0; padding: 0; }
  html, body { width: 1200px; height: 834px; overflow: hidden; }
  body {
    background: var(--stage);
    font-family: "Montserrat", Arial, sans-serif;
    position: relative;
  }
  .card {
    position: absolute;
    width: 560px;
    height: 320px;
    border-radius: 2px;
    overflow: hidden;
    box-shadow: 0 12px 30px rgba(0,0,0,0.45);
  }
  /* Front */
  .card-front {
    left: 70px; top: 70px;
    background: linear-gradient(135deg, var(--pink) 0%, #e4a8c8 55%, var(--pink-deep) 100%);
  }
  .front-name {
    position: absolute;
    top: 96px; left: 0; width: 100%;
    text-align: center;
    font-weight: 500;
    font-size: 34px;
    color: var(--white);
    letter-spacing: 0.5px;
  }
  .front-service {
    position: absolute;
    top: 200px; left: 0; width: 100%;
    text-align: center;
    font-size: 15px;
    color: #f3d7e7;
    letter-spacing: 0.4px;
  }
  .front-band {
    position: absolute;
    left: 0; width: 100%;
    top: 246px; height: 36px;
    background: var(--band);
  }
  /* Back */
  .card-back {
    left: 570px; top: 440px;
    background: linear-gradient(135deg, var(--white) 0%, var(--paper) 100%);
  }
  .brand {
    position: absolute;
    top: 58px; right: 40px;
    text-align: center;
  }
  .brand-name {
    font-size: 22px;
    font-weight: 500;
    color: var(--blue);
  }
  .brand-tagline {
    margin-top: 2px;
    font-size: 8px;
    letter-spacing: 2px;
    text-transform: uppercase;
    color: var(--pink-text);
  }
  .contact {
    position: absolute;
    left: 40px; bottom: 42px;
  }
  .contact-call {
    font-size: 26px;
    font-weight: 500;
    color: var(--pink-text);
    line-height: 1.05;
  }
  .contact-phone {
    font-size: 26px;
    font-weight: 600;
    color: var(--green);
    line-height: 1.1;
    margin-bottom: 10px;
  }
  .contact-line {
    display: flex;
    align-items: center;
    gap: 10px;
    font-size: 14px;
    color: var(--ink);
    line-height: 1.5;
  }
  .contact-line svg { width: 16px; height: 16px; flex: none; }
  .edge-stripe {
    position: absolute;
    left: 0; bottom: 0;
    width: 100%; height: 6px;
    display: flex;
  }
  .edge-stripe span { height: 100%; }
  .edge-pink { flex: 2.4; background: var(--pink); }
  .edge-purple { flex: 1.2; background: var(--purple); }
  .edge-green { flex: 1.4; background: var(--green); }
  .edge-blue { flex: 1; background: var(--blue); }
</style>
</head>
<body>
  <section class="card card-front" aria-label="Card front">
    <div class="front-name">Tilda Tinkerwire</div>
    <div class="front-service">Computer Care &amp; Repair</div>
    <div class="front-band"></div>
  </section>

  <section class="card card-back" aria-label="Card back">
    <div class="brand">
      <div class="brand-name">Tilda Tinkerwire</div>
      <div class="brand-tagline">Cherish Every Gadget</div>
    </div>

    <div class="contact">
      <div class="contact-call">Call Tilda</div>
      <div class="contact-phone">407-555-0148</div>
      <div class="contact-line">
        <svg viewBox="0 0 16 16" aria-hidden="true"><rect x="1.5" y="3.5" width="13" height="9" fill="none" stroke="#d89ac7" stroke-width="1.2"/><path d="M1.5 3.5 L8 9 L14.5 3.5" fill="none" stroke="#d89ac7" stroke-width="1.2"/></svg>
        <span>tilda.tinkerwire@postnest.com</span>
      </div>
      <div class="contact-line">
        <svg viewBox="0 0 16 16" aria-hidden="true"><circle cx="8" cy="8" r="6.5" fill="none" stroke="#d89ac7" stroke-width="1.2"/><ellipse cx="8" cy="8" rx="2.8" ry="6.5" fill="none" stroke="#d89ac7" stroke-width="1"/><line x1="1.5" y1="8" x2="14.5" y2="8" stroke="#d89ac7" stroke-width="1"/></svg>
        <span>www.tilda-tinkerwire.com</span>
      </div>
    </div>

    <div class="edge-stripe">
      <span class="edge-pink"></span>
      <span class="edge-purple"></span>
      <span class="edge-green"></span>
      <span class="edge-blue"></span>
    </div>
  </section>
</body>
</html>
```